現在ホームページリニューアルを検討しております。
社内でのデザインだとどうしても前情報がある分、発想の限界、偏りがどうしてもあります。

今回はなるべくフラットな状態でデザインを検討したいと考えておりますので、こちらで公募をさせていただくことにしました。

既存の歯科医院のデザインやイメージに縛られることなく、自由な発想でご提案頂きたいと思っております。

■依頼内容

PC・スマートフォン用 それぞれ1枚 合計2枚
(実装する際にはレスポンシブの予定です。)

診療科目は
小児
一般
矯正(大学から月に数回先生にお越し頂いています)

医院の特徴
ショッピングモール内にあります
駐車場あり
バリアフリー
お子さんの遊びスペースあり
デザイナー物件

ページ数
2ページ
希望イメージ
シンプル 複雑
単色 カラフル
暗い 明るい
日常 高級
遊び心 厳粛
未来的 伝統的
女性的 男性的
納品ファイル
• 高解像度JPG (.jpg)
• フォトショップ形式 (.psd)
• PNG形式 (.png)
▼弊社が用意するもの
・ページ構成
・テキスト
・ワイヤーフレーム
・ロゴ
・写真
※受注者様のご意向があれば、ビデオ通話などで対応することも可能です。
※ページ構成や画像などは、個別に送らせていただきたいので、まずはご提案またはメッセージにてご連絡ください。

▼依頼の流れ
1.ご提案
ご提案をいただき次第、弊社よりTOPページの構成をお送りします。
3.デザイン作成
デザインを作成しましたら、提案の【追記する】からデザインファイルの追加をしてください。
5.修正依頼
修正していただきたい箇所がある場合は、修正依頼をいたしますので、修正案を再提案してください。
6.納品
フォトショップ(psd)またはイラストレーター(ai)形式で納品をしていただきます。納品が完了次第、当選を行います。

弊社では、複数のWEBサイトを運用しております。
今回はTOPページのみの依頼となっておりますが、継続的に依頼をさせていただくことも考えております。
ご提案をお待ちしております。
ワイヤーフレームと写真素材を添付します。
依頼金額を45000円に変更して、延長しました。
たくさんのご応募ありがとうございます。
現在、選考中です。3~7日程度で当選デザインを決定できるかと思いますので、今しばらくお待ちください。

歯科医院スタッフの投票にて決定いたしました。

たくさんのご提案ありがとうございます。また機会があれば、是非よろしくお願いいたします。

```html
<!DOCTYPE html>
<html lang="ja">
<head>
<meta charset="utf-8">
<title>歯科医院 トップページ</title>
<link href="https://fonts.googleapis.com/css2?family=Noto+Sans+JP:wght@400;500;700&family=Roboto:wght@500;700&display=swap" rel="stylesheet">
<style>
:root{
  --blue:#4a86b8;
  --blue-deep:#3b78ad;
  --blue-pale:#dbe8f3;
  --gray-bg:#eeeeee;
  --ink:#333333;
  --white:#ffffff;
}
*{margin:0;padding:0;box-sizing:border-box}
html,body{width:1200px;height:4616px;overflow:hidden}
body{position:relative;background:var(--white);color:var(--ink);font-family:"Noto Sans JP",sans-serif}
.abs{position:absolute}

/* header */
.site-logo{left:40px;top:36px;font-size:30px;font-weight:500}
.tagline{left:140px;top:50px;font-size:12px;color:#666}
.header-tel{left:555px;top:48px;font-size:18px;color:var(--blue);font-weight:500}
.btn-reserve{left:724px;top:40px;width:104px;height:36px;background:var(--blue);color:var(--white);font-size:15px;display:flex;align-items:center;justify-content:center}
.schedule{border-collapse:collapse;font-size:15px;color:var(--white);background:var(--blue)}
.schedule td{border:2px solid var(--white);width:40px;height:44px;text-align:center}
.schedule td.label{width:46px;font-size:14px}
.dot{display:inline-block;width:20px;height:20px;border-radius:50%;background:var(--white)}
.header-schedule{left:912px;top:0}

/* hero */
.hero{left:0;top:112px;width:1200px;height:600px;background:linear-gradient(100deg,#dfe7ec 0%,#cdd9e0 45%,#e9d8cc 70%,#b9c7d3 100%)}
.hero-copy{left:148px;background:var(--blue);color:var(--white);font-size:21px;font-weight:500;padding:10px 18px}
.hero-sim{left:960px;top:552px;width:128px;height:128px;border-radius:50%;background:var(--blue);border:5px solid var(--white);color:var(--white);font-size:17px;font-weight:500;display:flex;align-items:center;justify-content:center;text-align:center;line-height:1.5}

/* nav */
.global-nav{left:0;top:738px;width:1200px;display:flex;justify-content:center;gap:70px;font-size:16px;font-weight:500}

/* section heads */
.sec-title{width:1200px;left:0;text-align:center;font-family:"Roboto","Noto Sans JP",sans-serif;font-size:34px;font-weight:700}
.sec-sub{width:1200px;left:0;text-align:center;font-size:12px}

/* guide */
.guide-band{left:0;top:872px;width:1200px;height:448px;background:var(--blue)}
.guide-photo{width:220px;height:220px;border-radius:50%;border:4px solid var(--white);background:linear-gradient(135deg,#cfdbe4,#a9bccb)}
.guide-label{width:200px;background:var(--blue);color:var(--white);padding:8px 12px;border:2px solid var(--white)}
.guide-label .name{font-size:14px;font-weight:500;border-bottom:1px solid var(--white);padding-bottom:4px;margin-bottom:4px}
.guide-label .desc{font-size:12px;line-height:1.5}

.stripe{left:0;width:1200px;height:24px;background:var(--blue-deep)}

/* concept */
.concept-photo{width:220px;height:220px;border-radius:110px 110px 0 0;background:linear-gradient(160deg,#e6eef4,#a8c4d8)}
.concept-box{width:220px;height:160px;background:var(--blue);color:var(--white);padding:22px 20px}
.concept-box .lead{font-size:17px;font-weight:500;line-height:1.6}
.concept-box .more{position:absolute;right:18px;bottom:16px;font-size:13px}

/* news */
.news-bg{left:0;top:2840px;width:1200px;height:780px;background:var(--gray-bg)}
.news-title{left:150px;top:2890px;font-family:"Roboto",sans-serif;font-size:34px;font-weight:700}
.news-sub{left:150px;top:2940px;font-size:12px}
.news-list{left:452px;top:2880px;width:720px;list-style:none}
.news-list li{height:70px;font-size:13px}
.news-list .date{display:inline-block;margin-right:12px}
.news-list .tag{display:inline-block;background:var(--blue);color:var(--white);font-size:10px;padding:1px 10px}
.news-list .text{margin-top:6px}

/* director */
.director-photo{left:152px;top:3740px;width:440px;height:300px;background:linear-gradient(180deg,#eef0f0,#c9ccc9)}
.director-box{left:592px;top:3740px;width:456px;height:300px;background:var(--blue);color:var(--white);padding:30px 36px}
.director-box h2{font-size:22px;font-weight:500;margin-bottom:14px}
.director-box p{font-size:15px;line-height:1.75}

/* footer */
.footer{left:0;top:4160px;width:1200px;height:456px;background:var(--blue);color:var(--white)}
.footer-logo{left:150px;top:40px;font-size:30px;font-weight:500}
.footer-tel{left:150px;top:104px;font-size:16px}
.footer-schedule{left:150px;top:140px}
.footer-schedule td{height:38px;width:36px}
.footer-nav{left:150px;top:314px;display:flex;gap:34px;font-size:13px}
.copyright{left:150px;top:350px;font-size:11px}
.footer-photo{left:592px;top:60px;width:488px;height:280px;background:linear-gradient(180deg,#f4f6f7,#c8d3da)}
</style>
</head>
<body>

<header>
  <div class="abs site-logo">Logo</div>
  <div class="abs tagline">ここにキャッチコピーが入ります</div>
  <div class="abs header-tel">TEL 000-12-3456</div>
  <div class="abs btn-reserve">WEB予約</div>
  <table class="abs schedule header-schedule">
    <tr><td class="label"></td><td>月</td><td>火</td><td>水</td><td>木</td><td>金</td><td>土</td></tr>
    <tr><td class="label">午前</td><td><span class="dot"></span></td><td><span class="dot"></span></td><td><span class="dot"></span></td><td><span class="dot"></span></td><td><span class="dot"></span></td><td><span class="dot"></span></td></tr>
    <tr><td class="label">午後</td><td><span class="dot"></span></td><td><span class="dot"></span></td><td><span class="dot"></span></td><td><span class="dot"></span></td><td><span class="dot"></span></td><td><span class="dot"></span></td></tr>
  </table>
</header>

<section>
  <div class="abs hero" role="img" aria-label="歯科医師が子どもの口の中を診察している写真"></div>
  <div class="abs hero-copy" style="top:452px">痛くない歯医者</div>
  <div class="abs hero-copy" style="top:516px">お子様連れでも安心の託児サービス</div>
  <div class="abs hero-copy" style="top:606px">何度も通院させない歯医者</div>
  <div class="abs hero-sim">治療シミュ<br>レーション</div>
</section>

<nav class="abs global-nav">
  <span>トップページ</span><span>トップページ</span><span>トップページ</span><span>トップページ</span><span>トップページ</span>
</nav>

<section>
  <div class="abs guide-band"></div>
  <div class="abs sec-title" style="top:918px;color:var(--white)">Guide</div>
  <div class="abs sec-sub" style="top:966px;color:var(--white)">診療案内</div>

  <div class="abs guide-photo" style="left:152px;top:1100px" role="img" aria-label="診療の様子の写真"></div>
  <div class="abs guide-label" style="left:240px;top:1246px"><div class="name">ここに治療名</div><div class="desc">ここに詳細の説明が入ります</div></div>
  <div class="abs guide-photo" style="left:452px;top:1100px" role="img" aria-label="歯科ユニットの写真"></div>
  <div class="abs guide-label" style="left:540px;top:1246px"><div class="name">ここに治療名</div><div class="desc">ここに詳細の説明が入ります</div></div>
  <div class="abs guide-photo" style="left:752px;top:1100px" role="img" aria-label="歯科模型の写真"></div>
  <div class="abs guide-label" style="left:840px;top:1246px"><div class="name">ここに治療名</div><div class="desc">ここに詳細の説明が入ります</div></div>

  <div class="abs guide-photo" style="left:152px;top:1440px" role="img" aria-label="子どもの診察の写真"></div>
  <div class="abs guide-label" style="left:240px;top:1586px"><div class="name">ここに治療名</div><div class="desc">ここに詳細の説明が入ります</div></div>
  <div class="abs guide-photo" style="left:452px;top:1440px" role="img" aria-label="矯正器具の写真"></div>
  <div class="abs guide-label" style="left:540px;top:1586px"><div class="name">ここに治療名</div><div class="desc">ここに詳細の説明が入ります</div></div>
  <div class="abs guide-photo" style="left:752px;top:1440px" role="img" aria-label="歯の模型の写真"></div>
  <div class="abs guide-label" style="left:840px;top:1586px"><div class="name">ここに治療名</div><div class="desc">ここに詳細の説明が入ります</div></div>

  <div class="abs guide-photo" style="left:152px;top:1760px" role="img" aria-label="治療中の写真"></div>
  <div class="abs guide-label" style="left:240px;top:1906px"><div class="name">ここに治療名</div><div class="desc">ここに詳細の説明が入ります</div></div>
  <div class="abs guide-photo" style="left:452px;top:1760px" role="img" aria-label="歯みがき指導の写真"></div>
  <div class="abs guide-label" style="left:540px;top:1906px"><div class="name">ここに治療名</div><div class="desc">ここに詳細の説明が入ります</div></div>
  <div class="abs guide-photo" style="left:752px;top:1760px" role="img" aria-label="笑顔の患者の写真"></div>
  <div class="abs guide-label" style="left:840px;top:1906px"><div class="name">ここに治療名</div><div class="desc">ここに詳細の説明が入ります</div></div>
</section>

<div class="abs stripe" style="top:2100px"></div>

<section>
  <div class="abs sec-title" style="top:2206px">Concept</div>
  <div class="abs sec-sub" style="top:2254px">コンセプト</div>

  <div class="abs concept-photo" style="left:180px;top:2340px" role="img" aria-label="歯科器具の写真"></div>
  <div class="abs concept-box" style="left:180px;top:2560px"><div class="lead">コンセプトがここに<br>入ります</div><div class="more">詳細はこちら</div></div>
  <div class="abs concept-photo" style="left:480px;top:2340px" role="img" aria-label="診療中の手元の写真"></div>
  <div class="abs concept-box" style="left:480px;top:2560px"><div class="lead">コンセプトがここに<br>入ります</div><div class="more">詳細はこちら</div></div>
  <div class="abs concept-photo" style="left:780px;top:2340px" role="img" aria-label="歯ブラシの写真"></div>
  <div class="abs concept-box" style="left:780px;top:2560px"><div class="lead">コンセプトがここに<br>入ります</div><div class="more">詳細はこちら</div></div>
</section>

<div class="abs stripe" style="top:2816px"></div>

<section>
  <div class="abs news-bg"></div>
  <div class="abs news-title">News</div>
  <div class="abs news-sub">お知らせ</div>
  <ul class="abs news-list">
    <li><span class="date">2019.01.01</span><span class="tag">NEWS</span><div class="text">ここに新着情報が入りますここに新着情報が入りますここに新着情報が入ります</div></li>
    <li><span class="date">2019.01.01</span><span class="tag">NEWS</span><div class="text">ここに新着情報が入りますここに新着情報が入りますここに新着情報が入ります</div></li>
    <li><span class="date">2019.01.01</span><span class="tag">NEWS</span><div class="text">ここに新着情報が入りますここに新着情報が入りますここに新着情報が入ります</div></li>
    <li><span class="date">2019.01.01</span><span class="tag">NEWS</span><div class="text">ここに新着情報が入りますここに新着情報が入りますここに新着情報が入ります</div></li>
    <li><span class="date">2019.01.01</span><span class="tag">NEWS</span><div class="text">ここに新着情報が入りますここに新着情報が入りますここに新着情報が入ります</div></li>
    <li><span class="date">2019.01.01</span><span class="tag">NEWS</span><div class="text">ここに新着情報が入りますここに新着情報が入りますここに新着情報が入ります</div></li>
    <li><span class="date">2019.01.01</span><span class="tag">NEWS</span><div class="text">ここに新着情報が入りますここに新着情報が入りますここに新着情報が入ります</div></li>
    <li><span class="date">2019.01.01</span><span class="tag">NEWS</span><div class="text">ここに新着情報が入りますここに新着情報が入りますここに新着情報が入ります</div></li>
    <li><span class="date">2019.01.01</span><span class="tag">NEWS</span><div class="text">ここに新着情報が入りますここに新着情報が入りますここに新着情報が入ります</div></li>
    <li><span class="date">2019.01.01</span><span class="tag">NEWS</span><div class="text">ここに新着情報が入りますここに新着情報が入りますここに新着情報が入ります</div></li>
  </ul>
</section>

<div class="abs stripe" style="top:3620px"></div>

<section>
  <div class="abs director-photo" role="img" aria-label="院内の待合スペースの写真"></div>
  <div class="abs director-box">
    <h2>医院長をが入ります</h2>
    <p>挨拶文がここに入ります挨拶文がここに入ります<br>挨拶文がここに入ります挨拶文がここに入ります<br>挨拶文がここに入ります挨拶文がここに入ります<br>挨拶文がここに入ります挨拶文がここに入ります<br>挨拶文がここに入ります挨拶文がここに入ります</p>
  </div>
</section>

<footer class="abs footer">
  <div class="abs footer-logo">Logo</div>
  <div class="abs footer-tel">TEL 000-12-3456　　WEB予約 &gt;&gt;</div>
  <table class="abs schedule footer-schedule">
    <tr><td class="label"></td><td>月</td><td>火</td><td>水</td><td>木</td><td>金</td><td>土</td></tr>
    <tr><td class="label">午前</td><td><span class="dot"></span></td><td><span class="dot"></span></td><td><span class="dot"></span></td><td><span class="dot"></span></td><td><span class="dot"></span></td><td><span class="dot"></span></td></tr>
    <tr><td class="label">午後</td><td><span class="dot"></span></td><td><span class="dot"></span></td><td><span class="dot"></span></td><td><span class="dot"></span></td><td><span class="dot"></span></td><td><span class="dot"></span></td></tr>
  </table>
  <div class="abs footer-nav"><span>トップページ</span><span>トップページ</span><span>トップページ</span><span>トップページ</span></div>
  <div class="abs copyright">All Right Reserved 2019</div>
  <div class="abs footer-photo" role="img" aria-label="白を基調とした診療室の写真"></div>
</footer>

</body>
</html>
```